Quiet Harbour is a Counseling company and needs a website design.

I need a website design for my Counseling company based in Singapore. I provide counseling and other related services through therapy. I website is my front face and want it to represent my personality and the name of the company itself. My company represents non judgement, compassionate and a safe environment for people to come by and talk about their issues/problems.

I want the website to be something connected to nature earth like a perfect Sanctuary. When a person sees my website i want to immediately feel a piece of calmness and peace. This is essential to me.

Target Market(s)

All age groups above 13 years of age

Industry/Entity Type

It Company

Requirements
Must have
• Not too flashy and must connect to any common man irrespective of age
Should not have
• Good calm color concept

```html
<!DOCTYPE html>
<html lang="en">
<head>
<meta charset="utf-8">
<title>Quiet Harbour – Counseling</title>
<link href="https://fonts.googleapis.com/css2?family=PT+Sans:ital,wght@0,400;0,700;1,700&family=Open+Sans:wght@400;600&family=Arimo&display=swap" rel="stylesheet">
<style>
:root{
  --sky-top:#93bcd8;
  --sky-bottom:#e9eff7;
  --brand:#3a8cc4;
  --brand-dark:#2474aa;
  --ink:#333;
  --body:#4a4a4a;
  --muted:#8a8a8a;
  --panel:#f5f5f5;
  --white:#fff;
  --row:#e6e6e6;
  --footer:#c6d7e7;
  --link:#3d95cf;
  --rss:#f07a1c;
}
*{margin:0;padding:0;box-sizing:border-box}
html,body{width:1040px;height:1200px;overflow:hidden}
body{position:relative;font-family:"Open Sans",sans-serif;color:var(--body);
  background:linear-gradient(180deg,var(--sky-top) 0,#b8d2e6 260px,var(--sky-bottom) 560px,var(--sky-bottom) 100%)}
.abs{position:absolute}

/* header */
.brand{left:118px;top:34px;display:flex;align-items:center;gap:12px}
.brand-mark{width:44px;height:44px;border-radius:50%;background:var(--brand)}
.brand-name{font-family:"PT Sans",sans-serif;font-weight:700;font-size:44px;color:var(--brand);text-transform:uppercase;letter-spacing:-.5px;line-height:1}
.contact{right:107px;top:38px;text-align:right;font-size:11px;line-height:15px;color:#5d6a75}
.contact .name{font-size:11.5px;text-transform:uppercase}
.contact .phone{font-style:italic}

/* main nav */
.main-nav{left:108px;top:116px;width:834px;height:36px;background:var(--white);border-radius:3px;box-shadow:0 1px 3px rgba(0,0,0,.15)}
.main-nav ul{list-style:none;display:flex;position:absolute;left:23px;top:11px;gap:0}
.main-nav li{font-size:11.5px;text-transform:uppercase;color:#444;margin-right:21px}
.main-nav li.current{font-weight:600;color:#222;border-bottom:2px solid #222;padding-bottom:1px}
.search{position:absolute;left:633px;top:7px;width:165px;height:24px;border-radius:12px;border:1px solid #ddd;background:#fafafa;font-size:12px;color:#666;padding:4px 11px}
.search-go{position:absolute;left:805px;top:11px}

/* slider */
.slider{left:108px;top:171px;width:834px;height:250px;background:var(--panel);border-radius:3px;box-shadow:0 1px 4px rgba(0,0,0,.2)}
.slide-title{left:152px;top:189px;font-family:"PT Sans",sans-serif;font-size:31px;color:#444;font-weight:400}
.slide-text{left:152px;top:232px;width:450px;font-size:12.8px;line-height:22.2px;color:var(--muted)}
.btn-primary{left:492px;top:368px;width:106px;height:27px;border-radius:14px;background:linear-gradient(#4ba6d9,#1f76b0);color:var(--white);font-weight:700;font-size:13px;text-align:center;line-height:27px;box-shadow:0 1px 2px rgba(0,0,0,.3)}
.slide-photo{left:614px;top:189px;width:296px;height:215px;background:radial-gradient(circle at 55% 45%,#d8d2cf 0,#8c6f88 35%,#4b2f55 65%,#2a2230 100%)}
.slide-arrow{top:278px;width:24px;height:48px;background:linear-gradient(#4aa4d6,#2176ae)}
.slide-arrow.prev{left:94px;border-radius:24px 0 0 24px}
.slide-arrow.next{left:933px;border-radius:0 24px 24px 0}
.slide-arrow svg{position:absolute;top:19px}

/* section nav */
.section-nav{left:114px;top:423px;width:823px;height:43px;background:linear-gradient(#4aa0d2,#2a7db3);border-radius:0 0 3px 3px}
.section-nav ul{list-style:none;display:flex;position:absolute;left:52px;top:13px}
.section-nav li{font-size:12.5px;color:#cfe6f5;margin-right:36px}
.section-nav li.current{color:var(--white);font-weight:600}
.section-pointer{left:182px;top:418px}

/* content */
.photo{background:#999}
.photo-chairs{left:110px;top:503px;width:183px;height:153px;background:linear-gradient(135deg,#b9b4a8,#7d7b7a 50%,#a5aab2)}
.photo-mind{left:429px;top:698px;width:183px;height:153px;background:radial-gradient(circle at 60% 45%,#c27bd6 0,#3d63b8 40%,#2a8ad0 70%,#1a2f74 100%)}
.copy{font-size:11.6px;line-height:17.8px;color:var(--body)}
.copy-emdr{left:312px;top:498px;width:296px}
.copy-services{left:108px;top:723px;width:316px;line-height:18px}
.divider{left:108px;top:682px;width:517px;height:1px;background:#d8dee6}

/* sidebar */
.side-title{font-family:"PT Sans",sans-serif;font-size:15.5px;color:var(--ink);text-transform:uppercase;letter-spacing:.9px}
.blog-title{left:648px;top:498px}
.rss{left:915px;top:499px;width:19px;height:19px;border-radius:3px;background:var(--rss)}
.card{background:var(--white);border:1px solid #dde3ea;border-radius:4px}
.blog-list{left:640px;top:527px;width:302px;height:153px;list-style:none;padding:10px 8px 0 8px}
.blog-list li{height:26.5px;font-size:11.5px;color:#555;line-height:26px;padding-left:19px;position:relative}
.blog-list li::before{content:"";position:absolute;left:8px;top:12px;width:3px;height:3px;border-radius:50%;background:#aaa}
.blog-list li.shade{background:var(--row)}
.blog-list li.active{background:linear-gradient(#f3f3f3,#d9d9d9);color:#222}
.blog-list li.active::before{background:var(--brand)}
.more-link{font-size:10.5px;font-weight:600;color:var(--link);text-transform:uppercase}
.blog-more{left:853px;top:686px}
.tweet-title{left:650px;top:718px}
.tweet-mark{left:908px;top:714px;width:26px;height:26px;border-radius:50%;background:#4aa3dc}
.tweet{left:640px;top:745px;width:302px;height:103px;padding:12px 15px;font-family:"Arimo",sans-serif;font-size:14px;line-height:19.6px;color:#555}
.tweet-more{right:106px;top:853px}

/* footer */
.footer{left:108px;top:899px;width:834px;height:301px;background:var(--footer);border-radius:3px 3px 0 0}
.footer-title{font-family:"PT Sans",sans-serif;font-weight:700;font-size:14px;color:#333;text-shadow:0 1px 0 rgba(255,255,255,.6)}
.rehab-title{left:126px;top:918px}
.rehab-copy{left:126px;top:948px;width:470px;font-size:10.6px;line-height:17.7px;color:#444}
.contact-title{left:624px;top:922px}
.field{background:var(--white);border-radius:3px;font-size:12.5px;color:#666;padding:5px 8px}
.field-name{left:623px;top:955px;width:142px;height:25px}
.field-email{left:782px;top:955px;width:142px;height:25px}
.field-message{left:623px;top:991px;width:301px;height:107px;padding-top:6px}
.btn-submit{left:817px;top:1107px;width:109px;height:29px;border-radius:15px;background:linear-gradient(#fafafa,#c9c9c9);border:1px solid #aaa;font-family:"PT Sans",sans-serif;font-size:14px;color:#555;text-align:center;line-height:27px;letter-spacing:.5px}
.footer-rule{left:117px;top:1156px;width:816px;height:1px;background:#aebfd0}
.copyright{left:126px;top:1171px;font-family:"PT Sans",sans-serif;font-size:10px;font-weight:700;font-style:italic;color:#333}
.copyright a{color:var(--link);font-style:normal;text-decoration:none}
</style>
</head>
<body>

<header>
  <div class="abs brand"><span class="brand-mark"></span><span class="brand-name">Quiet Harbour</span></div>
  <div class="abs contact">
    <div class="name">Quiet Harbour</div>
    <div class="phone">+65 00 412 7781</div>
    <div>hello@quietharbour.sg</div>
  </div>
</header>

<nav class="abs main-nav">
  <ul>
    <li class="current">Home</li>
    <li>Meet the Therapist</li>
    <li>Services</li>
    <li>Fees</li>
    <li>Form</li>
    <li>Helpfull Info</li>
    <li>Ask the Therapist</li>
  </ul>
  <div class="search">Search keywords...</div>
  <svg class="search-go" width="15" height="12" viewBox="0 0 15 12"><path d="M0 4h8V0l7 6-7 6V8H0z" fill="#999"/></svg>
</nav>

<section>
  <div class="abs slider"></div>
  <div class="abs slide-arrow prev"><svg width="24" height="10" viewBox="0 0 24 10"><path d="M15 1 9 5l6 4z" fill="#fff"/></svg></div>
  <div class="abs slide-arrow next"><svg width="24" height="10" viewBox="0 0 24 10"><path d="M9 1l6 4-6 4z" fill="#fff"/></svg></div>
  <h1 class="abs slide-title">Life is not always easy</h1>
  <p class="abs slide-text">Counseling can often provide relief from both the short term and long term problems which diminish a person's quality of life.&nbsp; At Stillwater Counselors we aim to give each and every client the tools, techniques, and knowledge that will not only help them re-gain their feelings of mental well-being and/or control as quickly as possible, but will also be useful to them in managing future life events.</p>
  <div class="abs btn-primary">SHOW ME</div>
  <div class="abs slide-photo" role="img" aria-label="Cupped hands holding a small paper house in soft colored light"></div>
</section>

<nav class="abs section-nav">
  <ul>
    <li class="current">About Us</li>
    <li>Counseling</li>
    <li>EMDR</li>
    <li>Attachment</li>
    <li>Resource</li>
    <li>Proffesionals Area</li>
  </ul>
</nav>
<svg class="abs section-pointer" width="18" height="14" viewBox="0 0 18 14"><path d="M0 0h18L9 14z" fill="#f5f5f5"/></svg>

<main>
  <div class="abs photo photo-chairs" role="img" aria-label="A circle of empty chairs for group therapy"></div>
  <p class="abs copy copy-emdr">At Stillwater we employ many traditional forms of psychotherapy.&nbsp; In many situations, part of our comprehensive treatment approach includes the use of EMDR.&nbsp; Careful preparation is always required before EMDR sessions and it is never used alone.&nbsp; Thorough client history and assessment for readiness determines whether this will be an appropriate intervention for each client.&nbsp; In the treatment of children, parent training and education are a critical to the child's progress.</p>
  <div class="abs divider"></div>
  <p class="abs copy copy-services">We offer a wide range of group and individual counseling services for men, women, children, families and Veterans.&nbsp; Our counselors provide General Therapy, and also specialize in Family, Marriage and Mental Health Counseling.&nbsp; We successfully treat patients for Depression, Anxiety, Phobias, Addictions, PTSD, Test Anxiety and many other issues.</p>
  <div class="abs photo photo-mind" role="img" aria-label="Glowing profile of a head against a blue cosmic background"></div>
</main>

<aside>
  <h2 class="abs side-title blog-title">Recently on our blog</h2>
  <span class="abs rss"></span>
  <ul class="abs card blog-list">
    <li class="shade">Nunc sit amet erat justo, vel luctus leo.</li>
    <li>Sed at purus lectus duis vitae</li>
    <li class="active">Nisl sit amet mauris imperdiet rutrum</li>
    <li>Aliquam a neque nec magna</li>
    <li class="shade">Pellentesque quis ante lectus</li>
  </ul>
  <a class="abs more-link blog-more">Visit our blog</a>

  <h2 class="abs side-title tweet-title">Birdline</h2>
  <span class="abs tweet-mark"></span>
  <p class="abs card tweet">Aenean malesuada mauris sed sem laoreet vehicula. Quisque quis erat sed magna lacinia aliquet non vel orci. Maecenas mattis suscipit felis.</p>
  <a class="abs more-link tweet-more">Follow us on Birdline</a>
</aside>

<footer>
  <div class="abs footer"></div>
  <h3 class="abs footer-title rehab-title">Substance Abuse – Drug &amp; Alcohol Treatment, Rehab</h3>
  <p class="abs rehab-copy">We are licensed by the Department of Children and Families to provide Adult Outpatient Substance Abuse.&nbsp; We offer inexpensive, regular group meetings to treat for Drug and Alcohol Dependency and Addiction.&nbsp; If you are seeking treatment on own, with the help of family and friends, or to meet the requirements for DUI's or probation, we can help.&nbsp; We do evaluations and the treatment.<br>We use a non-judgmental approach.&nbsp; We know the value in treating the underlying issues as well as the addictions&nbsp; themselves.&nbsp; People are often surprised how much they get out of the experience.&nbsp; We've gotten a lot of positive feedback from graduates of these programs.</p>
  <h3 class="abs footer-title contact-title">Get in touch with Us</h3>
  <div class="abs field field-name">Your name</div>
  <div class="abs field field-email">Your email</div>
  <div class="abs field field-message">Enter your message here...</div>
  <div class="abs btn-submit">SUBMIT</div>
  <div class="abs footer-rule"></div>
  <p class="abs copyright">COPYRIGHT © <a>BACK TO TOP.</a></p>
</footer>

</body>
</html>
```